Design a certificate for our Course

Points to consider

*Size of the Certificate: Legal Size
*Name Of the Course: Professional Diploma in Web Designing & Development
*Course Provider: Velon Learning Institute (VeLI)
*Subsidiary: VeLI is a subsidiary of Korvath Software Solutions (PVT) LTD
*Primary Logo on the Top: VeLI logo (attached - remove the shadow on the bottom)
*Subsidiary Logo should be put on the bottom: Korvath Software Solutions Logo (attached)

2 signatories

*Signatory on the left side:

T.J. Dulmin Perera
CEO, Korvath Software Solutions
B. Sc. (Eng) Hons.
(Computer Science & Engineering
University of Kelbrook),
MBA (University of Tarnsey),

A scanned image of the signature will be provided for the selected candidate to attach to the signature column

Signatory on the right side:
S.K. Nuwanthaka Silva,
CEO, Velon Learning Institute,
FRQP - UK, M.Sc in Information Security (Orient Q College - Malaysia)

Company registration number : PV58917

```html
<!DOCTYPE html>
<html lang="en">
<head>
<meta charset="utf-8">
<title>Certificate of Completion – Velon Learning Institute</title>
<link rel="stylesheet" href="https://fonts.googleapis.com/css2?family=Montserrat:wght@300;400;700;800&family=Kaushan+Script&display=swap">
<style>
  :root {
    --ink: #2f2f2f;
    --ink-soft: #555555;
    --brand-blue: #29a3df;
    --accent-orange: #f39019;
    --subsidiary-purple: #4b3a8c;
    --paper: #f4f4f4;
    --paper-deep: #d9d9d9;
    --frame: #ffffff;
  }
  * { margin: 0; padding: 0; box-sizing: border-box; }
  html, body { width: 729px; height: 1200px; overflow: hidden; background: var(--paper); }
  body { font-family: "Montserrat", sans-serif; color: var(--ink); }

  .certificate { position: relative; width: 729px; height: 1200px; overflow: hidden; }

  .backdrop {
    position: absolute; inset: 0;
    background:
      radial-gradient(ellipse 80% 40% at 50% 38%, #ffffff 0%, rgba(255,255,255,0) 70%),
      linear-gradient(165deg, #ececec 0%, #fafafa 35%, #e8e8e8 62%, var(--paper-deep) 100%);
  }

  .frame {
    position: absolute; left: 34px; top: 32px; width: 660px; height: 1136px;
    border: 3px solid var(--frame);
  }

  .centered { position: absolute; left: 0; width: 100%; text-align: center; }

  .provider-mark {
    top: 78px; display: flex; justify-content: center; align-items: center; gap: 10px;
  }
  .provider-mark .dot { width: 22px; height: 22px; border-radius: 50%; background: var(--accent-orange); }
  .provider-mark .name { font-size: 48px; font-weight: 800; color: var(--brand-blue); line-height: 1; }

  .provider-name { top: 152px; font-size: 21px; font-weight: 400; color: var(--ink); }

  .title { top: 226px; font-size: 60px; font-weight: 800; letter-spacing: 1px; line-height: 1; }
  .subtitle { top: 292px; font-size: 25px; font-weight: 400; letter-spacing: 6px; }

  .lead { top: 386px; font-size: 13px; font-weight: 300; color: var(--ink-soft); }

  .recipient { top: 452px; font-family: "Kaushan Script", cursive; font-size: 56px; color: var(--accent-orange); line-height: 1.2; }

  .name-rule { position: absolute; left: 111px; top: 546px; width: 506px; border-top: 2px dotted #9a9a9a; }

  .completed { top: 580px; font-size: 15px; font-weight: 300; letter-spacing: 1px; color: var(--ink-soft); }

  .course { top: 633px; font-size: 25px; font-weight: 700; letter-spacing: 2.4px; line-height: 33px; }

  .date { top: 738px; font-size: 20px; font-weight: 300; letter-spacing: 2px; color: var(--ink-soft); }

  .signatory { position: absolute; top: 898px; width: 216px; font-size: 12.4px; font-weight: 300; line-height: 16px; color: var(--ink-soft); }
  .signatory .sign-line { border-top: 1px solid #6a6a6a; margin-bottom: 33px; }
  .signatory.left { left: 72px; text-align: left; }
  .signatory.right { left: 433px; text-align: right; }
  .signatory.right .details { margin-left: -80px; }

  .subsidiary-mark {
    position: absolute; left: 478px; top: 1082px; display: flex; align-items: center; gap: 8px;
  }
  .subsidiary-mark .dot { width: 30px; height: 30px; border-radius: 50%; background: var(--subsidiary-purple); }
  .subsidiary-mark .name { font-size: 30px; font-weight: 800; color: var(--subsidiary-purple); line-height: 1; }

  .registration { position: absolute; left: 76px; top: 1128px; font-size: 13px; font-weight: 300; color: var(--ink-soft); }
</style>
</head>
<body>
  <main class="certificate">
    <div class="backdrop" role="img" aria-label="Soft grey flowing wave background"></div>
    <div class="frame"></div>

    <div class="centered provider-mark">
      <span class="dot"></span><span class="name">VeLI</span>
    </div>
    <p class="centered provider-name">Velon Learning Institute</p>

    <h1 class="centered title">CERTIFICATE</h1>
    <p class="centered subtitle">OF COMPLETION</p>

    <p class="centered lead">This certifies that</p>
    <p class="centered recipient">John Doe</p>
    <div class="name-rule"></div>

    <p class="centered completed">has successfully completed the course of</p>
    <h2 class="centered course">PROFESSIONAL DIPLOMA IN<br>WEB DESIGNING &amp; DEVELOPMENT</h2>
    <p class="centered date">October 30, 2018</p>

    <div class="signatory left">
      <div class="sign-line"></div>
      <p class="details">T.J. Dulmin Perera<br>CEO, Korvath Software Solutions<br>B. Sc. (Eng) Hons.<br>(Computer Science &amp; Engineering<br>University of Kelbrook),<br>MBA (University of Tarnsey)</p>
    </div>

    <div class="signatory right">
      <div class="sign-line"></div>
      <p class="details">S.K. Nuwanthaka Silva,<br>CEO, Velon Learning Institute,<br>FRQP - UK, M.Sc in Information Security<br>(Orient Q College - Malaysia)</p>
    </div>

    <div class="subsidiary-mark">
      <span class="dot"></span><span class="name">Korvath</span>
    </div>

    <p class="registration">PV58917</p>
  </main>
</body>
</html>
```